QDN Business Cards

I would like to use deep red (See attached logo), medium grays and white on the card to be used as separators for information using a white font over the red and gray colors. We are a web application design and development firm - specializing in custom software development with a content management solution. Our card needs to reflect innovative and cutting edge company.
I have attached the current card for content purposes - there is a front and back to the card. Open to suggestions on layout.

```html
<!DOCTYPE html>
<html lang="en">
<head>
<meta charset="utf-8">
<title>QDN Tech Group – Business Cards</title>
<link rel="stylesheet" href="https://fonts.googleapis.com/css2?family=Open+Sans:wght@400;600;700&display=swap">
<style>
  :root {
    --red-light: #d8232a;
    --red-deep: #8e181c;
    --red: #c1272d;
    --gray-dark: #3a3a3a;
    --gray-mid: #5c5c5c;
    --gray-bar: #6b6b6b;
    --white: #ffffff;
    --backdrop: #d9d9d9;
    --ink: #1e1e1e;
  }
  * { box-sizing: border-box; margin: 0; padding: 0; }
  html, body {
    width: 1200px; height: 900px; overflow: hidden;
    background: var(--backdrop);
    font-family: "Open Sans", Arial, sans-serif;
  }
  .canvas { position: relative; width: 1200px; height: 900px; }

  .card {
    position: absolute; width: 630px; height: 360px;
    box-shadow: 0 6px 18px rgba(0,0,0,.25);
  }

  /* Front (red) card */
  .card--front {
    left: 330px; top: 45px;
    background: linear-gradient(180deg, var(--red-light) 0%, var(--red-deep) 100%);
    color: var(--white);
  }
  .front__brand {
    position: absolute; left: 60px; top: 98px; width: 270px;
    font-size: 30px; font-weight: 600; line-height: 36px; white-space: nowrap;
    color: var(--white);
  }
  .front__web {
    position: absolute; left: 60px; top: 150px;
    font-size: 17px; font-weight: 600; white-space: nowrap;
  }
  .front__divider {
    position: absolute; left: 350px; top: 40px; width: 3px; height: 160px;
    background: var(--white);
  }
  .services {
    position: absolute; left: 378px; top: 40px; list-style: none;
    font-size: 16px; font-weight: 600; line-height: 17px; white-space: nowrap;
  }
  .front__follow {
    position: absolute; left: 60px; top: 262px;
    font-size: 16px; font-weight: 400; white-space: nowrap;
  }
  .social {
    position: absolute; left: 300px; top: 254px; display: flex; gap: 12px;
  }
  .social__dot {
    width: 32px; height: 32px; border-radius: 50%; background: var(--white);
  }

  /* Back (white) card */
  .card--back {
    left: 240px; top: 480px; background: var(--white); color: var(--gray-dark);
  }
  .back__brand {
    position: absolute; left: 50px; top: 106px; width: 280px;
    font-size: 30px; font-weight: 600; line-height: 36px; white-space: nowrap;
    color: var(--ink);
  }
  .back__tagline {
    position: absolute; left: 50px; top: 150px;
    font-size: 14px; font-weight: 600; color: var(--red); white-space: nowrap;
  }
  .person { position: absolute; left: 365px; top: 28px; }
  .person__name { font-size: 21px; font-weight: 700; color: var(--red); letter-spacing: .5px; white-space: nowrap; }
  .person__title { font-size: 15px; font-weight: 600; color: var(--gray-mid); margin-top: -2px; }
  .address {
    position: absolute; left: 365px; top: 110px;
    font-size: 15px; line-height: 20px; font-style: normal; color: var(--gray-mid);
    white-space: nowrap;
  }
  .contacts {
    position: absolute; left: 345px; top: 208px; list-style: none;
    font-size: 16px; color: var(--gray-mid); white-space: nowrap;
  }
  .contacts li { display: flex; align-items: center; gap: 9px; height: 23px; }
  .contacts svg { width: 19px; height: 19px; flex: none; }
  .bar {
    position: absolute; left: 70px; bottom: 0; width: 560px; height: 12px;
    display: flex;
  }
  .bar__gray { width: 45%; background: var(--gray-bar); height: 8px; }
  .bar__red { flex: 1; background: var(--red); align-self: flex-end; height: 12px; }
</style>
</head>
<body>
<main class="canvas">

  <section class="card card--front" aria-label="Card front">
    <div class="front__brand">QDN Tech Group</div>
    <div class="front__web">www.qdntechgroup.com</div>
    <div class="front__divider"></div>
    <ul class="services">
      <li>Project Mgmt/Strategy</li>
      <li>Web App Development</li>
      <li>Mobile App</li>
      <li>Design</li>
      <li>Section 508</li>
      <li>Training</li>
      <li>Staffing</li>
      <li>Social Media</li>
      <li>Advertising</li>
      <li>Marketing</li>
    </ul>
    <div class="front__follow">Follow Us @ qdntechgroup</div>
    <div class="social" aria-label="Social channels">
      <span class="social__dot"></span>
      <span class="social__dot"></span>
      <span class="social__dot"></span>
      <span class="social__dot"></span>
    </div>
  </section>

  <section class="card card--back" aria-label="Card back">
    <div class="back__brand">QDN Tech Group</div>
    <div class="back__tagline">Women Owned Small Business</div>

    <div class="person">
      <div class="person__name">DANA WHITMORE</div>
      <div class="person__title">President</div>
    </div>

    <address class="address">
      2250 Meridian Way<br>
      Suite 310 Easton, MD 21601
    </address>

    <ul class="contacts">
      <li>
        <svg viewBox="0 0 20 20" aria-hidden="true"><circle cx="10" cy="10" r="10" fill="var(--red)"/><rect x="7" y="4.5" width="6" height="11" rx="1" fill="none" stroke="#fff" stroke-width="1.4"/><circle cx="10" cy="13.3" r=".8" fill="#fff"/></svg>
        410.555.0147
      </li>
      <li>
        <svg viewBox="0 0 20 20" aria-hidden="true"><circle cx="10" cy="10" r="10" fill="var(--red)"/><path d="M6.5 5.5c1-.6 1.7 0 2.2 1.2.3.8 0 1.2-.6 1.6.5 1.3 1.3 2.2 2.6 2.8.5-.6 1-.9 1.7-.5 1.1.6 1.6 1.3.9 2.3-.8 1.1-2.6.9-4.5-.6-1.9-1.600-3.4-3.7-3.4-5.3 0-.7.4-1.2 1.1-1.5z" fill="#fff"/></svg>
        410.555.0182
      </li>
      <li>
        <svg viewBox="0 0 20 20" aria-hidden="true"><circle cx="10" cy="10" r="10" fill="var(--red)"/><rect x="5" y="8" width="10" height="6" rx="1" fill="#fff"/><rect x="7" y="4.5" width="6" height="4" fill="none" stroke="#fff" stroke-width="1.2"/><rect x="7" y="12" width="6" height="3.5" fill="var(--red)" stroke="#fff" stroke-width="1"/></svg>
        410.555.0196
      </li>
      <li>
        <svg viewBox="0 0 20 20" aria-hidden="true"><circle cx="10" cy="10" r="10" fill="var(--red)"/><rect x="4.5" y="6" width="11" height="8" fill="none" stroke="#fff" stroke-width="1.3"/><path d="M4.5 6l5.5 4.5L15.5 6" fill="none" stroke="#fff" stroke-width="1.3"/></svg>
        dana@qdntechgroup.com
      </li>
      <li>
        <svg viewBox="0 0 20 20" aria-hidden="true"><circle cx="10" cy="10" r="10" fill="var(--red)"/><circle cx="10" cy="10" r="5.5" fill="none" stroke="#fff" stroke-width="1.2"/><ellipse cx="10" cy="10" rx="2.3" ry="5.5" fill="none" stroke="#fff" stroke-width="1"/><path d="M4.5 10h11" stroke="#fff" stroke-width="1"/></svg>
        www.qdntechgroup.com
      </li>
    </ul>

    <div class="bar"><span class="bar__gray"></span><span class="bar__red"></span></div>
  </section>

</main>
</body>
</html>
```